Unique Brovek Building Bussiness Card Design

www.brovek.com.au

Please see website for Company profile. We require a design that incorporates our logo colours and is unique in shape and style compared to all other business cards.

www.brovek.com.au

INSPIRE US !!!
Updates

Target Market(s)

Facility managers, Building Managers, Architects

Industry/Entity Type

Business

Contact Information for Business Card

Brovek Property Works
Project Manager
Dalton Pryseworth
0437 916 248
Sales@brovek.com.au

Logo Text

Brovek Property Works

Logo styles of interest
Abstract Logo
Requirements
Nice to have
• Card must show we are an established big business to trust.

```html
<!DOCTYPE html>
<html lang="en">
<head>
<meta charset="utf-8">
<title>Brovek Property Works – Business Card</title>
<link rel="stylesheet" href="https://fonts.googleapis.com/css2?family=Arvo:wght@400;700&family=Saira+Condensed:wght@500&display=swap">
<style>
  :root {
    --page-bg: #f4f1ee;
    --card-bg: #ffffff;
    --brand-blue: #1f3f7a;
    --brand-orange: #e5652a;
    --name-red: #a8231f;
    --ink: #1c1c1c;
    --ink-soft: #333333;
  }
  * { box-sizing: border-box; margin: 0; padding: 0; }
  html, body {
    width: 1200px;
    height: 1000px;
    overflow: hidden;
    background: var(--page-bg);
  }
  .business-card {
    position: absolute;
    left: 226px;
    top: 203px;
    width: 726px;
    height: 450px;
    background: var(--card-bg);
    overflow: hidden;
  }
  .brand-lockup {
    position: absolute;
    left: 0;
    right: 0;
    top: 98px;
    display: flex;
    justify-content: center;
    align-items: center;
    gap: 12px;
  }
  .brand-mark {
    width: 30px;
    height: 30px;
    background: var(--brand-orange);
  }
  .brand-name {
    font-family: "Arvo", serif;
    font-weight: 700;
    font-size: 42px;
    line-height: 1;
    color: var(--brand-blue);
  }
  .person {
    position: absolute;
    left: 30px;
    width: 285px;
    top: 238px;
    text-align: center;
    font-family: "Saira Condensed", sans-serif;
    font-weight: 500;
  }
  .person-role {
    font-size: 25px;
    line-height: 1.1;
    color: var(--ink);
  }
  .person-name {
    font-size: 42px;
    line-height: 1.05;
    color: var(--name-red);
  }
  .divider {
    position: absolute;
    left: 355px;
    top: 234px;
    width: 2px;
    height: 108px;
    background: var(--brand-orange);
  }
  .contact {
    position: absolute;
    left: 390px;
    width: 320px;
    top: 248px;
    text-align: center;
    font-family: "Arvo", serif;
  }
  .contact-company {
    font-size: 18px;
    font-weight: 700;
    color: var(--brand-blue);
    line-height: 1.3;
  }
  .contact-phone {
    display: inline-flex;
    align-items: center;
    gap: 5px;
    font-size: 18px;
    color: var(--brand-blue);
    line-height: 1.35;
  }
  .contact-phone svg { width: 20px; height: 20px; }
  .contact-email {
    font-size: 18px;
    color: var(--ink-soft);
    line-height: 1.4;
  }
  .footer-rule {
    position: absolute;
    left: 0;
    right: 0;
    top: 392px;
    height: 6px;
    background: var(--brand-blue);
  }
  .footer-band {
    position: absolute;
    left: 0;
    right: 0;
    top: 398px;
    bottom: 0;
    background: var(--brand-orange);
  }
</style>
</head>
<body>
  <div class="business-card">
    <div class="brand-lockup">
      <span class="brand-mark"></span>
      <span class="brand-name">brovek.com.au</span>
    </div>

    <div class="person">
      <p class="person-role">Project Manager</p>
      <p class="person-name">Dalton Pryseworth</p>
    </div>

    <div class="divider"></div>

    <div class="contact">
      <p class="contact-company">Brovek Property Works</p>
      <p class="contact-phone">
        <svg viewBox="0 0 20 20" aria-hidden="true">
          <circle cx="10" cy="10" r="8.5" fill="none" stroke="#e5652a" stroke-width="1.6"/>
          <path d="M7 5.5c.6-.4 1.2-.2 1.5.4l.7 1.4c.2.5 0 1-.4 1.3l-.5.4c.5 1.2 1.3 2 2.5 2.5l.4-.5c.3-.4.8-.6 1.3-.4l1.4.7c.6.3.8.9.4 1.5-.6 1-1.7 1.4-2.8 1-2.4-.9-4.1-2.6-5-5-.4-1.1 0-2.2 1-2.8z" fill="#e5652a"/>
        </svg>
        0437 916 248
      </p>
      <p class="contact-email">Sales@brovek.com.au</p>
    </div>

    <div class="footer-rule"></div>
    <div class="footer-band"></div>
  </div>
</body>
</html>
```